Marrow Creek 381 Wine Label

Marrow Creek 381 Wine bottle label-
Pinot Noir, Chardonnay. Premium label.
Startup vineyard, Cool climate, Tasmania Australia.
Hills and Valley area, South East location
Needs to be a front and rear label as there are label requirements in Australia. Rear lable
is mearly to talk about the wine and have required information as per the examples uploaded

```html
<!DOCTYPE html>
<html lang="en">
<head>
<meta charset="utf-8">
<title>Marrow Creek 381 – Pinot Noir &amp; Chardonnay Label</title>
<link rel="stylesheet" href="https://fonts.googleapis.com/css2?family=Oranienbaum&family=Cormorant+Garamond:wght@500;600&family=Pinyon+Script&display=swap">
<style>
  :root {
    --page: #f3f0ec;
    --wine-deep: #2a0c13;
    --wine: #3a1219;
    --gold-light: #f2c22a;
    --gold: #dc9c16;
    --gold-dark: #b06a0e;
  }
  * { margin: 0; padding: 0; box-sizing: border-box; }
  html, body {
    width: 1200px;
    height: 1200px;
    overflow: hidden;
    background: var(--page);
  }
  .canvas {
    position: relative;
    width: 1200px;
    height: 1200px;
  }
  .front-label {
    position: absolute;
    left: 119px;
    top: 50px;
    width: 962px;
    height: 1100px;
    background: radial-gradient(ellipse at 50% 45%, var(--wine) 0%, var(--wine-deep) 100%);
    box-shadow: 0 6px 24px rgba(40, 10, 15, 0.25);
  }
  .front-label svg { display: block; }
  .gold-fill { fill: url(#goldSheen); }
  .gold-stroke { stroke: var(--gold); fill: none; stroke-width: 2; }
  .ornament { fill: url(#goldSoft); }
  .estate-name {
    font-family: "Cormorant Garamond", serif;
    font-weight: 600;
    font-size: 22px;
    letter-spacing: 4px;
  }
  .varietal-main {
    font-family: "Oranienbaum", serif;
    font-size: 138px;
  }
  .ampersand {
    font-family: "Pinyon Script", cursive;
    font-size: 88px;
  }
  .varietal-second {
    font-family: "Cormorant Garamond", serif;
    font-weight: 600;
    font-size: 48px;
  }
  .grade {
    font-family: "Cormorant Garamond", serif;
    font-weight: 600;
    font-size: 27px;
    letter-spacing: 11px;
  }
</style>
</head>
<body>
<main class="canvas">
  <section class="front-label" aria-label="Front wine label">
    <svg width="962" height="1100" viewBox="0 0 962 1100" xmlns="http://www.w3.org/2000/svg">
      <defs>
        <linearGradient id="goldSheen" x1="0" y1="0" x2="0" y2="1">
          <stop offset="0" stop-color="var(--gold-light)"/>
          <stop offset="0.55" stop-color="var(--gold)"/>
          <stop offset="1" stop-color="var(--gold-dark)"/>
        </linearGradient>
        <linearGradient id="goldSoft" x1="0" y1="0" x2="1" y2="1">
          <stop offset="0" stop-color="var(--gold-light)" stop-opacity="0.55"/>
          <stop offset="1" stop-color="var(--gold-dark)" stop-opacity="0.4"/>
        </linearGradient>
        <path id="secondVarietalArc" d="M303,615 A178 178 0 0 0 659,615"/>
      </defs>

      <!-- border bands -->
      <rect class="ornament band-top" x="0" y="57" width="962" height="33" role="img" aria-label="Gold diamond pattern border"/>
      <rect class="ornament band-bottom" x="0" y="1008" width="962" height="33" role="img" aria-label="Gold diamond pattern border"/>

      <!-- estate line -->
      <line class="gold-stroke" x1="262" y1="251" x2="330" y2="251"/>
      <line class="gold-stroke" x1="632" y1="251" x2="700" y2="251"/>
      <text class="estate-name gold-fill" x="483" y="259" text-anchor="middle">MARROW CREEK 381</text>

      <!-- crest ornaments -->
      <rect class="ornament" x="306" y="306" width="108" height="56" rx="28" role="img" aria-label="Gold scroll flourish"/>
      <rect class="ornament" x="548" y="306" width="108" height="56" rx="28" role="img" aria-label="Gold scroll flourish"/>
      <rect class="ornament" x="425" y="290" width="112" height="182" rx="56" role="img" aria-label="Gold grape cluster with vine leaf"/>

      <!-- crest frame -->
      <line class="gold-stroke" x1="381" y1="364" x2="381" y2="485"/>
      <line class="gold-stroke" x1="581" y1="364" x2="581" y2="485"/>

      <!-- main varietal -->
      <text class="varietal-main gold-fill" x="481" y="589" text-anchor="middle" textLength="512" lengthAdjust="spacingAndGlyphs">PINOT NOIR</text>
      <line class="gold-stroke" x1="224" y1="600" x2="737" y2="600"/>

      <!-- lower arc: line sits outside the curved text -->
      <path class="gold-stroke" d="M288,615 A193 193 0 0 0 674,615"/>
      <circle class="gold-fill" cx="291" cy="650" r="3.5"/>
      <circle class="gold-fill" cx="671" cy="650" r="3.5"/>
      <text class="ampersand gold-fill" x="481" y="680" text-anchor="middle">&amp;</text>
      <text class="varietal-second gold-fill">
        <textPath href="#secondVarietalArc" startOffset="50%" text-anchor="middle">CHARDONNAY</textPath>
      </text>

      <!-- base ornament -->
      <rect class="ornament" x="290" y="812" width="382" height="34" rx="17" role="img" aria-label="Gold scroll flourish beneath crest"/>

      <text class="grade gold-fill" x="486" y="884" text-anchor="middle">PREMIUM</text>
    </svg>
  </section>
</main>
</body>
</html>
```